I am a highly experienced private practice psychotherapist serving high end clientele in the Wall Street area of New York City. I need electronic letterhead (that can also be printed) to use for bills, receipts, and correspondences.

My clients are very high end and are used to elegance and wealth. The letterhead should contain the following information: Marian T. Holcombe, LCSW 72 Pellham Street, Suite 2561 New York, NY 10087 Phone : (917) 555-3194 email: therapy@marianholcombelcsw.example website: www.marianholcombelcsw.example

Thank you for your designs. Please be advised that the letterhead will be used for bills/invoices; professional letters to other mental health professionals and doctors, as well as to attorneys. It needs to be highly professional in the same way that a law firm has professional and elegant letterhead, raher than whimsical or with spa designers. My letters end up as official documents.

```html
<!DOCTYPE html>
<html lang="en">
<head>
<meta charset="utf-8">
<title>Marian T. Holcombe, LCSW — Letterhead</title>
<link rel="stylesheet" href="https://fonts.googleapis.com/css2?family=Cinzel:wght@600&family=Arimo&display=swap">
<style>
  :root {
    --paper: #ffffff;
    --ink: #111111;
    --rule: #1a1a1a;
    --damask-tone: #d9d9d9;
    --link: #1a3ccf;
  }
  html, body {
    margin: 0;
    padding: 0;
    overflow: hidden;
    background: var(--paper);
  }
  .letterhead {
    position: relative;
    width: 848px;
    height: 1200px;
    background: var(--paper);
    overflow: hidden;
  }
  .damask-band {
    position: absolute;
    top: 0;
    right: 0;
    width: 428px;
    height: 1200px;
    background:
      linear-gradient(to right, rgba(255,255,255,1) 0%, rgba(255,255,255,0.55) 30%, rgba(255,255,255,0) 75%),
      linear-gradient(to bottom, #ececec 0%, var(--damask-tone) 45%, #e4e4e4 100%);
  }
  .masthead {
    position: absolute;
    top: 52px;
    left: 51px;
    margin: 0;
    font-family: "Cinzel", serif;
    font-weight: 600;
    font-size: 36px;
    letter-spacing: 0.5px;
    line-height: 1;
    color: var(--ink);
  }
  .masthead-rule {
    position: absolute;
    top: 102px;
    left: 44px;
    width: 744px;
    height: 4px;
    background: var(--rule);
  }
  .contact-footer {
    position: absolute;
    left: 0;
    right: 0;
    top: 1141px;
    text-align: center;
    font-family: "Arimo", Arial, sans-serif;
    font-size: 16px;
    line-height: 20px;
    color: var(--ink);
  }
  .contact-footer p { margin: 0; }
  .contact-footer a { color: var(--link); text-decoration: underline; }
</style>
</head>
<body>
  <div class="letterhead">
    <div class="damask-band" role="img" aria-label="Soft grey damask pattern fading in from the right edge"></div>
    <h1 class="masthead">Marian T. Holcombe, LCSW</h1>
    <div class="masthead-rule"></div>
    <footer class="contact-footer">
      <p>72 Pellham Street, Suite 2561 New York, NY 10087 | Phone: (917) 555-3194</p>
      <p>Email: therapy@marianholcombelcsw.example | Website: <a href="#">www.marianholcombelcsw.example</a></p>
    </footer>
  </div>
</body>
</html>
```